Stylish new business card needed!

Hello everyone! I am in need of a new business card design for an alarm company here in Hurricane WV. I have all fonts, color codes and logos provided for you use! We are a young company and like the style of a clean sleek looking business card. Would like it double sided, one side holding the logo and the other with your design!
Target Market(s)
The people that are looking for the newest tech for home automation and security
Industry/Entity Type
Alarm services; Home automation
Contact Information for Business Card
Name of person; position (Sales; Installer); Phone Number (555.418.7290); Employee cell Number; Website (www.GuardedByVemlo.example); Employee Email; Double sided
Look and feel
Each slider illustrates characteristics of the customer's brand and the style your logo design should communicate.

```html
<!DOCTYPE html>
<html lang="en">
<head>
<meta charset="utf-8">
<title>Vemlo business card</title>
<link href="https://fonts.googleapis.com/css2?family=Montserrat:wght@400;500;600;700;800&display=swap" rel="stylesheet">
<style>
  :root{
    --backdrop:#b0b0b0;
    --paper:#ffffff;
    --orange:#ff7a3d;
    --slate:#8fa3a3;
    --white:#ffffff;
  }
  *{box-sizing:border-box;margin:0;padding:0}
  html,body{width:1154px;height:1200px;overflow:hidden}
  body{background:var(--backdrop);font-family:"Montserrat",sans-serif;position:relative}
  .card{position:absolute;left:206px;width:724px;height:435px;background:var(--paper)}
  .card--front{top:108px}
  .card--back{top:665px}

  .front-kicker{position:absolute;top:106px;left:0;width:100%;text-align:center;
    color:var(--orange);font-weight:800;font-size:33px;letter-spacing:1px}
  .front-name{position:absolute;top:150px;left:0;width:100%;display:flex;justify-content:center;align-items:center;gap:14px}
  .front-name .wordmark{color:var(--slate);font-weight:400;font-size:118px;letter-spacing:4px;line-height:1}
  .front-name .dot{width:30px;height:30px;border-radius:50%;background:var(--orange)}
  .front-tagline{position:absolute;top:309px;left:0;width:100%;text-align:center;
    color:var(--orange);font-weight:800;font-size:14px;letter-spacing:.6px}

  .back-name{position:absolute;top:100px;left:63px;display:flex;align-items:center;gap:10px}
  .back-name .wordmark{color:var(--slate);font-weight:400;font-size:60px;letter-spacing:2px;line-height:1}
  .back-name .dot{width:16px;height:16px;border-radius:50%;background:var(--orange)}

  .person-band{position:absolute;top:212px;left:0;width:341px;height:77px;background:var(--orange);
    padding:19px 0 0 59px;color:var(--white)}
  .person-name{font-weight:700;font-size:21px;letter-spacing:.6px;line-height:1.1}
  .person-role{font-weight:400;font-size:15px;margin-top:2px}

  .contacts{position:absolute;top:208px;left:376px;list-style:none}
  .contacts li{display:flex;align-items:center;height:37px;color:var(--slate);font-size:16.5px;font-weight:500;letter-spacing:.3px}
  .contacts svg{width:22px;height:22px;margin-right:14px;flex:none}
</style>
</head>
<body>
  <section class="card card--front">
    <p class="front-kicker">GUARDED BY</p>
    <div class="front-name"><span class="wordmark">VEMLO</span><span class="dot"></span></div>
    <p class="front-tagline">AUTOMATION AND SECURITY SERVICES</p>
  </section>

  <section class="card card--back">
    <div class="back-name"><span class="wordmark">VEMLO</span><span class="dot"></span></div>
    <div class="person-band">
      <p class="person-name">NAME OF PERSON</p>
      <p class="person-role">Installer</p>
    </div>
    <ul class="contacts">
      <li>
        <svg viewBox="0 0 24 24" aria-hidden="true"><path fill="var(--orange)" d="M6.6 10.8c1.4 2.8 3.8 5.1 6.6 6.6l2.2-2.2c.3-.3.7-.4 1-.2 1.1.4 2.3.6 3.6.6.6 0 1 .4 1 1V20c0 .6-.4 1-1 1C10.6 21 3 13.4 3 4c0-.6.4-1 1-1h3.5c.6 0 1 .4 1 1 0 1.3.2 2.5.6 3.6.1.3 0 .7-.2 1z"/></svg>
        555 418 7290
      </li>
      <li>
        <svg viewBox="0 0 24 24" aria-hidden="true"><rect x="6.5" y="2.5" width="11" height="19" rx="1.5" fill="none" stroke="var(--orange)" stroke-width="2"/><circle cx="12" cy="18" r="1" fill="var(--orange)"/></svg>
        000 000 0000
      </li>
      <li>
        <svg viewBox="0 0 24 24" aria-hidden="true"><g fill="none" stroke="var(--orange)" stroke-width="2"><circle cx="12" cy="12" r="9.5"/><ellipse cx="12" cy="12" rx="4" ry="9.5"/><path d="M2.5 12h19M4 7h16M4 17h16"/></g></svg>
        www.GuardedByVemlo.example
      </li>
      <li>
        <svg viewBox="0 0 24 24" aria-hidden="true"><rect x="1.5" y="5" width="21" height="14" fill="var(--orange)"/><path d="M1.5 5l10.5 8 10.5-8M1.5 19l8-7M22.5 19l-8-7" fill="none" stroke="var(--white)" stroke-width="1.5"/></svg>
        info@guardedbyvemlo.example
      </li>
    </ul>
  </section>
</body>
</html>
```